Consumer facing site as a spin off of primary B2B site

Create a consumer-focused website for a product that transforms TVs into digital frames, based on primary digital signage website https://lumo-reel.com.
Requirements
1. Homepage
• Hero Section: Engaging imagery of the product in use in home settings, with a clear, concise value proposition.
• Introduction Video: A short, engaging video that explains the product's key features and benefits.
• Clear Product Value Proposition: "Transform your TVs into shared family albums", "Easily connect with loved ones through photos and videos", etc.
• How It Works: A simple step-by-step guide or infographic showing how easy it is to set up and use.
• Testimonials: Snippets from real users showcasing how the product has enhanced their home and family life.
• Visual appeal: Images of the product in use (families enjoying content, simple setup on TVs)
• Clear Calls to Action: "Try for Free," "Learn More"
2. Product Details Page
• Features Overview: Detailed descriptions of key features, including screen size flexibility, connectivity, social features, and interactivity.
• Simplify Feature Language: Avoid technical jargon, focus on benefits for families (easy sharing, remote management, slideshow options)
• Showcase Scenarios: "Share baby photos with grandparents", "Keep in touch while traveling", "Send video messages for birthdays"
• Technical Specifications: Information on app compatibility, resolution support, storage options, and any hardware requirements.
• Gallery: High-resolution images showing the product's interface, app screenshots, and examples of it being used in various home environments.
3. FAQ & Support
• Frequently Asked Questions: Answers to common queries about setup, compatibility, subscriptions, and troubleshooting.
• Setup Guides and Tutorials: Step-by-step instructions and video tutorials for setting up and personalizing the product.
• Customer Support: Contact form, live chat, and support hotline information for users needing assistance.
4. Pricing & Subscription Plans
• Details on pricing for the app/service, with a comparison chart if multiple tiers are offered.
• Subscription Benefits: A breakdown of what's included in the subscription, such as cloud storage, exclusive features, and any family sharing options.
• Free Trial Offer: Information on how to start a free trial, what it includes, and how users can subscribe afterward.
5. About Us
• Our Story: Background on LumoReel, the team, and the mission behind the product.
• Vision for Families: Explanation of how the product aims to bring families closer together.
• Sustainability and Social Responsibility
Also need a quick UI refresh (Style/Icons) for the companion mobile app. See attached document

```html
<!DOCTYPE html>
<html lang="en">
<head>
<meta charset="utf-8">
<title>LumoReel – Transform Spaces Digitally</title>
<link rel="stylesheet" href="https://fonts.googleapis.com/css2?family=Lexend:wght@300;400;500;600;700&display=swap">
<style>
:root{
  --navy:#0e1045;
  --ink:#111322;
  --muted:#5b5e72;
  --blue:#2a33d6;
  --band-a:#1c1f8c;
  --band-b:#3d43e8;
  --card:#f3f4f8;
  --white:#ffffff;
  --star:#f5b400;
}
*{margin:0;padding:0;box-sizing:border-box}
html,body{width:1200px;height:5124px;overflow:hidden}
body{font-family:"Lexend",sans-serif;color:var(--ink);background:var(--white);position:relative}
.abs{position:absolute}
.btn{display:inline-flex;align-items:center;justify-content:center;border-radius:30px;font-size:11px;font-weight:400;height:30px;padding:0 16px;white-space:nowrap}
.btn-dark{background:var(--navy);color:#fff}
.btn-blue{background:var(--blue);color:#fff}
.btn-ghost{border:1.5px solid var(--navy);color:var(--navy);background:#fff}
.eyebrow{font-size:17px;font-weight:500;color:var(--ink)}
.eyebrow::before{content:"";display:inline-block;width:2px;height:15px;background:var(--ink);margin-right:7px;vertical-align:-2px}
.h2{font-size:37px;font-weight:600;line-height:1.05;color:var(--ink)}
.photo{border-radius:10px}

/* nav */
.nav{top:0;left:0;width:1200px;height:60px}
.logo{display:flex;align-items:center;gap:8px;font-size:19px;font-weight:600;color:var(--navy)}
.logo .dot{width:26px;height:26px;border-radius:50%;background:var(--navy)}
.menu{top:14px;left:304px;display:flex;align-items:center;font-size:11px;color:var(--ink)}
.menu span{padding:0 12px}
.menu .active{background:var(--navy);color:#fff;border-radius:20px;height:32px;display:flex;align-items:center;padding:0 20px}
.nav-icons{top:22px;left:984px;display:flex;gap:6px}
.nav-icons i{width:18px;height:18px;border:1.5px solid var(--ink);border-radius:50%;display:block}

/* hero */
.hero{top:62px;left:14px;width:1180px;height:564px;border-radius:16px;background:linear-gradient(90deg,#1a1d4c 0%,#3a3f6a 35%,#b89c86 70%,#d9c7b5 100%)}
.hero-card{top:230px;left:48px;width:442px;height:248px;border-radius:14px;background:rgba(255,255,255,.22);border:1px solid rgba(255,255,255,.35);padding:20px}
.hero-card h1{font-size:44px;font-weight:600;color:#fff;line-height:1.02}
.hero-card p{font-size:10.5px;color:#eef0ff;line-height:1.4;margin-top:14px;width:400px}
.hero-ctas{display:flex;gap:14px;margin-top:22px;align-items:center}
.play-sm{width:28px;height:28px;border-radius:50%;border:1.5px solid #fff;display:flex;align-items:center;justify-content:center}
.avatars{top:504px;left:48px;display:flex}
.avatars span{width:44px;height:44px;border-radius:50%;border:2px solid #fff;margin-right:-8px;background:linear-gradient(135deg,#c9a287,#6f5443)}
.avatars .plus{background:rgba(255,255,255,.3);display:flex;align-items:center;justify-content:center;color:#fff;font-size:24px}
.see-reviews{top:562px;left:48px;color:#fff;font-size:16px;font-weight:600;border-bottom:1.5px solid #fff;width:196px;padding-bottom:6px;display:flex;justify-content:space-between}
.scroll{top:618px;left:592px;width:18px;height:26px;border:1.5px solid var(--ink);border-radius:10px;background:#fff}

/* about */
.about-1{top:742px;left:162px;width:226px;height:404px;background:linear-gradient(180deg,#27356a,#6b7ca8 60%,#30406e)}
.about-2{top:710px;left:404px;width:224px;height:226px;background:linear-gradient(180deg,#eceae6,#a6b6cd 60%,#7f6d5f)}
.about-3{top:948px;left:404px;width:224px;height:146px;background:linear-gradient(135deg,#3b3128,#a88a66 55%,#2f2a26)}
.about-orb{top:1000px;left:388px;width:124px;height:124px;border-radius:50%;background:radial-gradient(circle at 70% 30%,#fff,#c8c9d4 50%,#3d3f55)}
.about-text{top:752px;left:655px;width:340px}
.points{margin-top:20px;display:flex;flex-direction:column;gap:26px;position:relative}
.point{display:flex;gap:12px;align-items:center}
.point i{width:34px;height:34px;border-radius:50%;background:var(--navy);flex:none}
.point p{font-size:10px;color:var(--ink);line-height:1.4}
.founder{top:1066px;left:766px;display:flex;gap:10px;align-items:center}
.founder .av{width:30px;height:30px;border-radius:50%;background:linear-gradient(135deg,#d6b49d,#7c5b47)}
.founder b{font-size:13px;font-weight:500;display:block}
.founder small{font-size:10px;color:var(--muted)}

/* video */
.center-head{left:0;width:1200px;text-align:center}
.video{top:1312px;left:14px;width:1180px;height:484px;border-radius:14px;background:linear-gradient(90deg,#2b2421,#6b5443 30%,#9a8f93 50%,#6e5647 70%,#3b2f2a)}
.play-big{top:1510px;left:556px;width:88px;height:88px;border-radius:50%;background:rgba(255,255,255,.35);display:flex;align-items:center;justify-content:center}

/* product info */
.info{top:1888px;left:152px;width:420px}
.info .h2{font-size:35px;white-space:nowrap}
.info-copy{font-size:10px;line-height:1.45;color:var(--ink);margin-top:22px;width:360px}
.features{display:grid;grid-template-columns:220px 160px;row-gap:14px;margin-top:8px}
.feat{display:flex;gap:8px;align-items:center;font-size:13px;line-height:1.05}
.feat svg{flex:none}
.p-img1{top:1870px;left:600px;width:216px;height:230px;background:linear-gradient(135deg,#6a5a4c,#c2a788 50%,#5a4a3f)}
.p-img2{top:1896px;left:826px;width:226px;height:206px;background:linear-gradient(180deg,#f0ece7,#b9927d 60%,#6f5546)}
.p-img3{top:2110px;left:726px;width:326px;height:170px;background:linear-gradient(135deg,#1b1a22,#6a5442 55%,#2b2420)}

/* value band */
.band{top:2356px;left:14px;width:1180px;height:126px;border-radius:14px;background:linear-gradient(90deg,var(--band-a),var(--band-b) 50%,var(--band-a));display:flex;align-items:center;justify-content:center}
.stat{display:flex;align-items:center;gap:12px;color:#fff;font-size:15px;line-height:1.15;padding:0 28px}
.sep{width:1.5px;height:40px;background:rgba(255,255,255,.7)}

/* pricing */
.toggle{top:2640px;left:0;width:1200px;display:flex;justify-content:center;align-items:center;gap:14px;font-size:14px;font-weight:600}
.toggle span{font-size:10px;font-weight:400;border-radius:20px;height:32px;padding:0 14px;display:flex;align-items:center}
.plan{top:2708px;width:290px;height:388px;background:var(--card);border-radius:6px;text-align:center;padding-top:28px}
.plan h4{font-size:13px;font-weight:400}
.plan .price{font-size:38px;font-weight:600;margin-top:10px}
.plan .offer{font-size:12.5px;margin-top:12px;padding-bottom:14px;border-bottom:2px dashed #8c8e9c;margin-left:14px;margin-right:14px}
.plan ul{list-style:none;font-size:10.5px;line-height:1.38;color:var(--ink);margin-top:18px;padding:0 28px}
.plan ul li{margin-bottom:4px}
.plan .foot{position:absolute;left:14px;right:14px;top:312px;border-top:2px dashed #8c8e9c;padding-top:18px}

/* faq */
.faq-left{top:3260px;left:152px;width:350px}
.faq-left p{font-size:11px;line-height:1.5;color:var(--ink);margin-top:20px}
.faq-open{top:3262px;left:546px;width:506px;height:134px;border-radius:8px;background:linear-gradient(90deg,var(--band-a),var(--band-b));color:#fff;padding:18px 12px}
.faq-open h5{font-size:15px;font-weight:400}
.faq-open p{font-size:10px;line-height:1.5;margin:16px 0 0 38px;width:380px;color:#e2e4ff}
.faq-row{left:556px;width:490px;display:flex;justify-content:space-between;align-items:center;font-size:15px}
.chev{width:26px;height:26px;border-radius:50%;background:var(--ink);display:flex;align-items:center;justify-content:center}

/* contact */
.contact{top:3582px;left:14px;width:1180px;height:280px;border-radius:14px;background:linear-gradient(90deg,#2f3070 0%,#2a2f98 45%,#2d35d6 100%)}
.contact-text{top:3648px;left:698px;color:#fff}
.contact-text .eyebrow{color:#fff}
.contact-text .eyebrow::before{background:#fff}

/* steps */
.step{width:210px;text-align:center}
.step .ico{width:58px;height:58px;border-radius:50%;background:#fff;box-shadow:0 2px 10px rgba(0,0,0,.18);margin:0 auto;display:flex;align-items:center;justify-content:center}
.step h6{font-size:14px;font-weight:500;margin-top:14px}
.step p{font-size:10.5px;line-height:1.5;color:var(--muted);margin-top:12px}

/* reviews */
.r-main{top:4470px;left:466px;width:288px;height:310px;background:linear-gradient(180deg,#f4f4f4,#b9a392 45%,#3c342e)}
.r-s1{top:4604px;left:158px;width:134px;height:172px;background:linear-gradient(180deg,#cfd8d9,#c79f84 50%,#9ca9ab)}
.r-s2{top:4604px;left:312px;width:134px;height:172px;background:linear-gradient(180deg,#f2ead9,#a6836b 50%,#2f3e5c)}
.r-text{top:4484px;left:776px;width:280px}
.arrows{display:flex;gap:22px;margin-top:36px}
.arrow{width:58px;height:36px;display:flex;align-items:center;justify-content:center}

/* footer */
.footer{top:4866px;left:14px;width:1180px;height:258px;border-radius:14px 14px 0 0;background:linear-gradient(90deg,var(--band-a),var(--band-b) 60%,#2b32c8);color:#fff}
.footer .logo{color:#fff}
.footer .logo .dot{background:#fff}
.flink{position:absolute;font-size:10.5px;color:#fff;text-decoration:underline;white-space:nowrap}
.fine{font-size:8.5px;display:flex;gap:16px;white-space:nowrap}
.fine a{color:#fff;text-decoration:underline}
.socials{display:flex;gap:18px}
.socials i{width:20px;height:20px;border-radius:50%;border:1.5px solid #fff;display:block}
</style>
</head>
<body>

<header class="abs nav">
  <div class="abs logo" style="top:14px;left:48px"><span class="dot"></span>LumoReel</div>
  <nav class="abs menu">
    <span class="active">Home</span><span>About Us</span><span>Product</span><span>Pricing &amp; Subscription Plans</span><span>FAQ &amp; Support</span><span>Contact Us</span>
  </nav>
  <div class="abs nav-icons"><i></i><i></i></div>
  <a class="abs btn btn-dark" style="top:14px;left:1040px;height:34px;padding:0 18px">Get Started</a>
</header>

<section>
  <div class="abs hero" role="img" aria-label="Family laughing on a couch with popcorn while using a TV remote"></div>
  <div class="abs hero-card">
    <h1>Transform Spaces<br>Digitally</h1>
    <p>Lorem Ipsum Dolor Sit Amet Consectetur. Purus Dignissim Rutrum Morbi Sed Volutpat Et Ultrices Nulla Mi. Posuere Egestas Sed Sit Venenatis Lectus Turpis Nec Laoreet. Eget Suspendisse Hendrerit Neque Cras Et.</p>
    <div class="hero-ctas">
      <a class="btn btn-dark" style="height:34px">Try LumoReel Free</a>
      <span style="display:flex;align-items:center;gap:6px;color:#fff;font-size:11px">
        <span class="play-sm"><svg width="10" height="10" viewBox="0 0 10 10"><path d="M2 1l7 4-7 4z" fill="#fff"/></svg></span>See Video
      </span>
    </div>
  </div>
  <div class="abs avatars" role="img" aria-label="Reviewer portraits">
    <span></span><span></span><span></span><span class="plus">+</span>
  </div>
  <div class="abs see-reviews"><span>See All Reviews</span><span>›</span></div>
  <div class="abs scroll"></div>
</section>

<section>
  <div class="abs photo about-1" role="img" aria-label="Friends watching a movie together with popcorn"></div>
  <div class="abs photo about-2" role="img" aria-label="Family looking at a laptop together"></div>
  <div class="abs photo about-3" role="img" aria-label="Cozy living room with a TV showing a photo"></div>
  <div class="abs about-orb" role="img" aria-label="Decorative glossy sphere"></div>
  <div class="abs about-text">
    <div class="eyebrow">About Us</div>
    <h2 class="h2" style="margin-top:14px">Crafting Futures<br>Together</h2>
    <div class="points">
      <svg class="abs" style="left:16px;top:30px" width="2" height="140"><line x1="1" y1="0" x2="1" y2="140" stroke="#111322" stroke-dasharray="3 3"/></svg>
      <div class="point"><i></i><p>Lorem Ipsum Dolor Sit Amet Consectetur.<br>Commodo Leo Nunc Risus Lobortis Porttitor. Duis.</p></div>
      <div class="point"><i></i><p>Lorem Ipsum Dolor Sit Amet Consectetur.<br>Commodo Leo Nunc Risus Lobortis Porttitor. Duis.</p></div>
      <div class="point"><i></i><p>Lorem Ipsum Dolor Sit Amet Consectetur.<br>Commodo Leo Nunc Risus Lobortis Porttitor. Duis.</p></div>
    </div>
  </div>
  <a class="abs btn btn-dark" style="top:1070px;left:655px">Learn More</a>
  <div class="abs founder"><span class="av" role="img" aria-label="Founder portrait"></span><div><b>Maren Holt</b><small>The Founder</small></div></div>
</section>

<section>
  <div class="abs center-head" style="top:1218px"><div class="eyebrow">Product Introduction</div><h2 class="h2" style="margin-top:10px">Watch Learn Decide</h2></div>
  <div class="abs video" role="img" aria-label="Family cheering while watching a football game on a large TV"></div>
  <div class="abs play-big"><svg width="34" height="34" viewBox="0 0 34 34"><path d="M8 4l22 13-22 13z" fill="#fff"/></svg></div>
</section>

<section>
  <div class="abs info">
    <div class="eyebrow">Product Info &amp; Feature</div>
    <h2 class="h2" style="margin-top:12px">Uncover Every Nuance<br>Embrace Brilliance</h2>
    <p class="info-copy">Lorem Ipsum Dolor Sit Amet Consectetur. Purus Dignissim Rutrum Morbi Sed Volutpat Et Ultrices Nulla Mi. Posuere Egestas Sed Sit Venenatis Lectus Turpis Nec Laoreet. Eget Suspendisse Hendrerit Neque Cras Et.</p>
    <div style="font-size:15px;font-weight:500;margin-top:12px">Feature</div>
    <div class="features">
      <div class="feat"><svg width="38" height="34" viewBox="0 0 38 34" fill="none" stroke="#111322" stroke-width="1.6"><rect x="2" y="2" width="34" height="22" rx="2"/><path d="M14 30h10M19 24v6"/></svg>Centralized Content<br>Management</div>
      <div class="feat"><svg width="38" height="34" viewBox="0 0 38 34" fill="none" stroke="#111322" stroke-width="1.6"><rect x="3" y="3" width="12" height="12" rx="2"/><rect x="23" y="3" width="12" height="12" rx="2"/><rect x="3" y="19" width="12" height="12" rx="2"/><rect x="23" y="19" width="12" height="12" rx="2"/></svg>Remote<br>Control</div>
      <div class="feat"><svg width="38" height="34" viewBox="0 0 38 34" fill="none" stroke="#111322" stroke-width="1.6"><path d="M4 30h30M8 30V18M16 30V10M24 30V16M32 30V4"/></svg>Analytics &amp;<br>Reporting</div>
      <div class="feat"><svg width="38" height="34" viewBox="0 0 38 34" fill="none" stroke="#111322" stroke-width="1.6"><rect x="8" y="3" width="22" height="28" rx="2"/><path d="M13 11h12M13 17h12M13 23h8"/></svg>Content<br>Rotation</div>
    </div>
    <a class="btn btn-dark" style="margin-top:22px">Learn More</a>
  </div>
  <div class="abs photo p-img1" role="img" aria-label="Group of friends relaxing on a sofa watching TV"></div>
  <div class="abs photo p-img2" role="img" aria-label="Smiling family of four indoors"></div>
  <div class="abs photo p-img3" role="img" aria-label="Bowl of popcorn in front of a glowing TV"></div>
</section>

<section class="abs band">
  <div class="stat"><svg width="36" height="36" viewBox="0 0 36 36" fill="none" stroke="#fff" stroke-width="1.8"><circle cx="18" cy="18" r="14"/><path d="M11 18l5 5 9-10"/></svg>Unmatched<br>Quality</div><span class="sep"></span>
  <div class="stat"><svg width="36" height="36" viewBox="0 0 36 36" fill="none" stroke="#fff" stroke-width="1.8"><rect x="4" y="6" width="12" height="10"/><rect x="20" y="6" width="12" height="10"/><rect x="4" y="20" width="12" height="10"/><rect x="20" y="20" width="12" height="10"/></svg>Client<br>Satisfaction</div><span class="sep"></span>
  <div class="stat"><svg width="36" height="36" viewBox="0 0 36 36" fill="none" stroke="#fff" stroke-width="1.8"><circle cx="18" cy="11" r="6"/><path d="M6 32c1-8 6-12 12-12s11 4 12 12"/></svg>Expert &amp;<br>Experience</div><span class="sep"></span>
  <div class="stat"><svg width="36" height="36" viewBox="0 0 36 36" fill="none" stroke="#fff" stroke-width="1.8"><path d="M18 4l4 8 9 1-7 6 2 9-8-5-8 5 2-9-7-6 9-1z"/></svg>Continuous<br>Support</div><span class="sep"></span>
  <div class="stat"><svg width="36" height="36" viewBox="0 0 36 36" fill="none" stroke="#fff" stroke-width="1.8"><circle cx="16" cy="16" r="11"/><circle cx="16" cy="16" r="5"/><path d="M24 24l8 8"/></svg>Focus On<br>Results</div>
</section>

<section>
  <div class="abs center-head" style="top:2552px"><div class="eyebrow">Pricing &amp; Subscription Plans</div><h2 class="h2" style="margin-top:10px">Affordable Choices Premium Experiences</h2></div>
  <div class="abs toggle"><span class="btn-blue">Annual</span>OR<span style="border:1.5px solid var(--ink)">Monthly</span></div>

  <div class="abs plan" style="left:150px">
    <h4>Basic</h4><div class="price">$10.00</div><div class="offer">Limited Offer! First MonthFree</div>
    <ul><li>Up To 2 Screens</li><li>PDF</li><li>Up To 25 Pages</li><li>Droid Screen, Orchard OS, Ember Stick, Tessa OS</li></ul>
    <div class="foot"><a class="btn btn-blue">Book Now</a></div>
  </div>
  <div class="abs plan" style="left:458px">
    <h4>Pro</h4><div class="price">$30.00</div><div class="offer">Limited Offer! First MonthFree</div>
    <ul><li>Up To 10 Screens</li><li>PDF</li><li>Unlimited Pages, Images Or Slides</li><li>Droid Screen, Orchard OS, Ember Stick, Tessa OS</li><li>Email Support</li><li>99% SLA Uptime</li></ul>
    <div class="foot"></div>
  </div>
  <div class="abs plan" style="left:766px">
    <h4>Enterprise</h4><div class="price">$Custom</div><div class="offer" style="color:transparent">&nbsp;</div>
    <ul><li>Unlimited Screens</li><li>App Pro Content Plus Animation</li><li>Unlimited Pages, Images Or Slides</li><li>Droid Screen, Orchard OS, Ember Stick, Tessa OS</li><li>Email Support</li><li>Custom SLAs</li></ul>
    <div class="foot"><a class="btn btn-blue">Book Now</a></div>
  </div>
  <a class="abs btn btn-dark" style="top:3134px;left:544px">Learn More</a>
</section>

<section>
  <div class="abs faq-left">
    <div class="eyebrow">FAQ</div>
    <h2 class="h2" style="margin-top:10px;font-size:35px;white-space:nowrap">Your Answers Await</h2>
    <p>Lorem Ipsum Dolor Sit Amet Consectetur. Pellentesque Velit Pellentesque Euismod Accumsan Egestas Cursus. Id Diam Augue Consequat Diam Quis Vel Varius Mattis Elementum.</p>
  </div>
  <a class="abs btn btn-dark" style="top:3452px;left:152px">Learn More</a>
  <a class="abs btn btn-ghost" style="top:3452px;left:252px">Ask Your Questions</a>
  <div class="abs faq-open">
    <h5>(01)&nbsp; Lorem Ipsum Dolor Sit Amet Consectetur.</h5>
    <span class="abs chev" style="top:14px;right:12px;background:#fff"><svg width="12" height="12" viewBox="0 0 12 12"><path d="M2 4l4 4 4-4" stroke="#111322" stroke-width="2" fill="none"/></svg></span>
    <p>Lorem Ipsum Dolor Sit Amet Consectetur. Pellentesque Velit Pellentesque Euismod Accumsan Egestas Cursus. Id Diam Augue Consequat Diam Quis Vel Varius Mattis Elementum. Massa Lorem Purus Mauris.</p>
  </div>
  <div class="abs faq-row" style="top:3420px"><span>(02)&nbsp; Lorem Ipsum Dolor Sit Amet Consectetur.</span><span class="chev"><svg width="12" height="12" viewBox="0 0 12 12"><path d="M4 2l4 4-4 4" stroke="#fff" stroke-width="2" fill="none"/></svg></span></div>
  <div class="abs faq-row" style="top:3460px"><span>(03)&nbsp; Lorem Ipsum Dolor Sit Amet Consectetur.</span><span class="chev"><svg width="12" height="12" viewBox="0 0 12 12"><path d="M4 2l4 4-4 4" stroke="#fff" stroke-width="2" fill="none"/></svg></span></div>
</section>

<section>
  <div class="abs contact" role="img" aria-label="Friends enjoying a show together, tinted blue"></div>
  <div class="abs contact-text">
    <div class="eyebrow">Contact Us</div>
    <h2 class="h2" style="color:#fff;margin-top:14px">Let's Talk – Your<br>Success Starts Here</h2>
    <a class="btn" style="background:#fff;color:var(--ink);margin-top:28px">Contact Now</a>
  </div>
</section>

<section>
  <div class="abs center-head" style="top:3954px"><div class="eyebrow">How It Works</div><h2 class="h2" style="margin-top:10px">Step-By-Step Guide</h2></div>
  <svg class="abs" style="top:4060px;left:250px" width="720" height="150" viewBox="0 0 720 150" fill="none" stroke="#555" stroke-dasharray="4 4" stroke-width="1.2">
    <path d="M40 28 C140 20 200 60 236 112"/>
    <path d="M262 112 C320 50 400 20 462 24"/>
    <path d="M490 24 C560 30 640 60 690 112"/>
  </svg>
  <div class="abs step" style="top:4052px;left:152px">
    <div class="ico"><svg width="30" height="30" viewBox="0 0 30 30" fill="#0e1045"><circle cx="15" cy="8" r="4"/><circle cx="6" cy="11" r="3"/><circle cx="24" cy="11" r="3"/><path d="M8 26c0-6 3-10 7-10s7 4 7 10z"/><path d="M1 24c0-5 2-8 5-8s3 2 3 2l-2 6z"/><path d="M29 24c0-5-2-8-5-8s-3 2-3 2l2 6z"/></svg></div>
    <h6>Lorem Ipsum Dolor Sit</h6>
    <p>Lorem Ipsum Dolor Sit Amet Consectetur. Venenatis Ut Augue Tempor Ultrices. Vitae Tempor Pretium Dolor At Est Et. Enim Sem Turpis Vel Turpis. Pulvinar Non Egestas Cum Velit Bibendum Dolor. In Massa Lectus Eget Magna. Bibendum.</p>
  </div>
  <div class="abs step" style="top:4140px;left:382px">
    <div class="ico"><svg width="30" height="30" viewBox="0 0 30 30" fill="#0e1045"><path d="M4 4h9v9H4zM17 17h9v9h-9z"/><path d="M17 4h9v9h-9zM4 17h9v9H4z" fill="none" stroke="#0e1045" stroke-width="2"/></svg></div>
    <h6>Lorem Ipsum Dolor Sit Amet</h6>
    <p>Lorem Ipsum Dolor Sit Amet Consectetur. Egestas Quam Quis Hendrerit Viverra A. Penatibus Adipiscing Tristique Faucibus A Ullamcorper Suspendisse Lectus. Et Felis.</p>
  </div>
  <div class="abs step" style="top:4052px;left:612px">
    <div class="ico"><svg width="30" height="30" viewBox="0 0 30 30"><circle cx="15" cy="15" r="12" fill="#0e1045"/><path d="M9 15l4 4 8-9" stroke="#fff" stroke-width="2.4" fill="none"/></svg></div>
    <h6>Lorem Ipsum Dolor Sit Amet</h6>
    <p>Lorem Ipsum Dolor Sit Amet Consectetur. Volutpat Orci Arcu Quis Mauris Suscipit Viverra. In Neque Ultrices Ut Nisl Lorem Congue Morbi Morbi Vivamus. Magna Ac Non.</p>
  </div>
  <div class="abs step" style="top:4140px;left:842px">
    <div class="ico"><svg width="30" height="30" viewBox="0 0 30 30" fill="none" stroke="#0e1045" stroke-width="2.4"><path d="M5 25L25 5M5 5l20 20"/><circle cx="15" cy="15" r="4" fill="#0e1045"/></svg></div>
    <h6>Lorem Ipsum Dolor Sit Amet</h6>
    <p>Lorem Ipsum Dolor Sit Amet Consectetur. Neque Interdum Fermentum Metus Interdum Imperdiet Aliquam. Arcu Dictum Tristique Viverra Id Adipiscing Tempus. Sapien.</p>
  </div>
</section>

<section>
  <div class="abs" style="top:4462px;left:152px">
    <div class="eyebrow">Client Reviews</div>
    <h2 class="h2" style="margin-top:10px">The Heartbeat<br>Of Our Success.</h2>
  </div>
  <div class="abs photo r-s1" role="img" aria-label="Portrait of a smiling woman"></div>
  <div class="abs photo r-s2" role="img" aria-label="Portrait of a smiling man in a patterned shirt"></div>
  <div class="abs photo r-main" role="img" aria-label="Portrait of a young man in a hat"></div>
  <div class="abs r-text">
    <div style="font-size:14px;font-weight:500">Dorian Vale</div>
    <div style="font-size:10px;color:var(--muted);margin-top:10px">Global Directives Architect</div>
    <p style="font-size:10.5px;line-height:1.5;margin-top:22px;color:var(--ink)">Lorem ipsum dolor sit amet consectetur. Cursus tortor gravida lobortis tellus. Urna in eros auctor quam egestas magnis congue velit fames. Adipiscing natoque fermentum sodales massa. Viverra auctor leo eu arcu libero etiam urna. Sem odio pellentesque in auctor eget hendrerit.</p>
    <div style="color:var(--star);font-size:16px;letter-spacing:4px;margin-top:10px">★★★★<span style="color:#f5dc9a">★</span></div>
    <div class="arrows">
      <span class="arrow"><svg width="50" height="14" viewBox="0 0 50 14" fill="none" stroke="#111322" stroke-width="2"><path d="M48 7H3M9 1L2 7l7 6"/></svg></span>
      <span class="arrow"><svg width="50" height="14" viewBox="0 0 50 14" fill="none" stroke="#111322" stroke-width="2"><path d="M2 7h45M41 1l7 6-7 6"/></svg></span>
    </div>
  </div>
</section>

<footer class="abs footer">
  <div class="abs logo" style="top:58px;left:138px"><span class="dot"></span>LumoReel</div>
  <p class="abs" style="top:118px;left:138px;width:340px;font-size:10px;line-height:1.4">Lorem Ipsum Dolor Sit Amet Consectetur. Habitasse Sed Commodo Dictumst Tristique. Senectus Adipiscing Aliquam Id Cras Tellus. Lorem Enim Quis Sit Ac P</p>
  <a class="flink" style="top:122px;left:524px">Home</a>
  <a class="flink" style="top:122px;left:594px">About Us</a>
  <a class="flink" style="top:122px;left:682px">Shop</a>
  <a class="flink" style="top:122px;left:750px">Contact Us</a>
  <a class="flink" style="top:122px;left:850px">New &amp; Media</a>
  <a class="flink" style="top:122px;left:960px">Legal Notic</a>
  <a class="flink" style="top:150px;left:524px">Terms &amp; Condication</a>
  <a class="flink" style="top:150px;left:674px">Privacy Policy</a>
  <a class="flink" style="top:150px;left:788px">Help &amp; Support</a>
  <a class="flink" style="top:150px;left:910px">News Letter</a>
  <div class="abs" style="top:184px;left:138px;width:904px;height:1px;background:rgba(255,255,255,.7)"></div>
  <div class="abs socials" style="top:208px;left:138px"><i></i><i></i><i></i></div>
  <div class="abs fine" style="top:212px;left:542px"><a>Privacy Policy</a><a>Terms Of Service</a><a>Cookies Settings</a><span>Copyright ©2024 All Right Reserved</span></div>
</footer>

</body>
</html>
```